Create a book cover for velmora QPL

We are looking for a designer to design a cover for a log book in two versions. The two versions only have a slight difference in page count and text, other than that, it is one design.

The main color is blue. No black, no white except book title and other text. The cover must closely relate to the interior pages provided in the attachment. The style should be simple and modern, no old school graphics and fonts. Apply color psychology in the design. Please be creative and you are allowed to use download templates and graphic elements, but you must provide commercial licenses.

Here are the basic information of the book:
1. Book title: MOTOR CARE TRACKER JOURNAL
2. Book size: 6x9 inches
3. Page count: 61 (version 1) and 73 (version 2)
4. Platform: velmora qpl

Requirement for version 1:
1. Front cover: book title
2. Spine: no book title and author name
3. Back cover: text on the top and pen name logo on the bottom middle
4. Back cover text:
• Your essential tool for tracking vehicle health and maintenance
• Dedicated sections for maintenance schedules and repair history
• Track up to 30 maintenance schedules and repair history
• Easy-to-use tables and clear layouts
• Perfect for all car owners, from enthusiasts to everyday drivers

We hope it helps you keep your vehicle in excellent condition. Please take a moment to leave a positive review on Velmora and share your experience if you find it helpful. Thank you!

Requirement for version 2:
1. Front cover: book title ,text "COLOR PAGES"
4. Back cover text:
• Track up to 36 maintenance schedules and repair history

Export:
1. Cover design in PDF and editable file format.
2. Sources/Commercial licenses for everything you did not create by yourself including fonts.

```html
<!DOCTYPE html>
<html lang="en">
<head>
<meta charset="utf-8">
<title>Motor Care Tracker Journal – Cover Spread</title>
<link href="https://fonts.googleapis.com/css2?family=Bebas+Neue&family=Montserrat:wght@500&family=Allison&display=swap" rel="stylesheet">
<style>
  :root {
    --navy: #011a54;
    --navy-deep: #0a1536;
    --white: #ffffff;
    --yellow: #fdd835;
    --logo-ring: #9aa3b5;
    --logo-fill: #1c2536;
  }
  * { margin: 0; padding: 0; box-sizing: border-box; }
  html, body { width: 1200px; height: 1200px; overflow: hidden; background: var(--navy); }
  .canvas { position: relative; width: 1200px; height: 1200px; background: var(--navy); }

  .spread {
    position: absolute; left: 59px; top: 196px; width: 1082px; height: 808px;
    background: var(--navy);
    box-shadow: 0 0 60px 20px rgba(6, 12, 34, 0.75);
  }

  .title { position: absolute; text-align: center; color: var(--white); }
  .title-main, .title-sub { font-family: "Bebas Neue", sans-serif; line-height: 1; display: block; }
  .title-script {
    display: block; font-family: "Allison", cursive; color: var(--yellow);
    line-height: 1; font-weight: 400;
  }

  /* back cover */
  .back-title { left: 150px; top: 38px; width: 346px; }
  .back-title .title-main { font-size: 96px; letter-spacing: 1px; }
  .back-title .title-sub { font-size: 51px; margin-top: 2px; letter-spacing: 0.5px; }
  .back-title .title-script { font-size: 92px; margin-top: -28px; }

  .features {
    position: absolute; left: 26px; top: 272px; width: 560px; list-style: none;
    font-family: "Montserrat", sans-serif; font-weight: 500; font-size: 13.4px;
    color: var(--white); letter-spacing: 0.2px;
  }
  .features li { height: 31px; }
  .features li::before { content: "• "; }

  .closing {
    position: absolute; left: 26px; top: 446px; width: 520px;
    font-family: "Montserrat", sans-serif; font-weight: 500; font-size: 13.4px;
    line-height: 18px; color: var(--white); letter-spacing: 0.2px;
  }

  .pen-name {
    position: absolute; left: 208px; top: 588px; width: 128px; height: 128px;
    border-radius: 50%; background: var(--logo-fill);
    border: 4px solid var(--logo-ring);
    display: flex; align-items: center; justify-content: center;
    font-family: "Bebas Neue", sans-serif; font-size: 27px; color: var(--white);
  }

  /* front cover */
  .front-title { left: 574px; top: 40px; width: 470px; }
  .front-title .title-main { font-size: 176px; letter-spacing: 4px; }
  .front-title .title-sub { font-size: 96px; margin-top: -4px; letter-spacing: 0.5px; }
  .front-title .title-script { font-size: 170px; margin-top: -60px; }

  .service-icon {
    position: absolute; left: 613px; top: 502px; width: 380px; height: 206px;
    border-radius: 24px;
    background: linear-gradient(135deg, var(--yellow), #f3cc2e);
  }
</style>
</head>
<body>
<div class="canvas">
  <section class="spread">
    <!-- back cover -->
    <div class="title back-title">
      <span class="title-main">MOTOR</span>
      <span class="title-sub">CARE TRACKER</span>
      <span class="title-script">journal</span>
    </div>

    <ul class="features">
      <li>Your essential tool for tracking vehicle health and maintenance</li>
      <li>Dedicated sections for maintenance schedules and repair history</li>
      <li>Track up to 30 maintenance schedules and repair history</li>
      <li>Easy-to-use tables and clear layouts</li>
      <li>Perfect for all car owners, from enthusiasts to everyday drivers</li>
    </ul>

    <p class="closing">We hope it helps you keep your vehicle in excellent condition.<br>Please take a moment to leave a positive review on Velmora and<br>share your experience if you find it helpful. Thank you!</p>

    <div class="pen-name">DORIAN VALES</div>

    <!-- front cover -->
    <div class="title front-title">
      <span class="title-main">MOTOR</span>
      <span class="title-sub">CARE TRACKER</span>
      <span class="title-script">journal</span>
    </div>

    <div class="service-icon" role="img" aria-label="Yellow icon of a car beside a gear with a wrench"></div>
  </section>
</div>
</body>
</html>
```